Redesign This Psychology Website

We would like a slight redesign of this successful psychology (relationship counselling) website:

www.TheWillowNook.com.au

We are updating the website, and we'd like a slight refresh of the design and style.

Please keep to very similar colours, and use the same logo. We're looking for around 10 page templates, however the main one is the home page.

Keep in mind, this website already converts quite well, so we want a new, fresh design in keeping with this one. Please don't bother designing something too extremely different.

thanks :)

Target Market(s)

couples who are looking for relationship counselling. Men and women, 25 - 70, across Australia

Industry/Entity Type

Psychology

Number of Pages Required

5+ page

Font styles to use
Sans Serif

Colors
87cfc6
b7a5cd
ec1f27
ffffff
cee9f5

Requirements
Must have
• a similar look to the current design, just looking for a slight refresh.
• Search bar
• Areas for lots of photos
• same logo
• lots of content areas
Nice to have
• great content areas, where we can display a lot of content and our areas.
Should not have
• no colors like orange, etc.
• should not have a totally different feel.

```html
<!DOCTYPE html>
<html lang="en">
<head>
<meta charset="utf-8">
<title>The Willow Nook – Relationship Counselling</title>
<link href="https://fonts.googleapis.com/css2?family=Open+Sans:wght@400;600;700&family=Raleway:wght@400;600;700&display=swap" rel="stylesheet">
<style>
:root{
  --teal:#1b8b92;
  --teal-dark:#137179;
  --teal-soft:#87cfc6;
  --lilac:#b7a5cd;
  --red:#e0242c;
  --red-dark:#b81a21;
  --sky:#cee9f5;
  --page:#eef6f8;
  --white:#ffffff;
  --ink:#3d4a50;
  --muted:#6f7b80;
  --line:#d6e4e8;
}
*{box-sizing:border-box;margin:0;padding:0}
html,body{width:1200px;height:5341px;overflow:hidden}
body{background:var(--page);font-family:"Open Sans",Arial,sans-serif;color:var(--ink);font-size:15px;line-height:1.6}
h1,h2,h3,h4{font-family:"Raleway","Open Sans",sans-serif}
a{color:inherit;text-decoration:none}
.wrap{width:1030px;margin:0 auto;position:relative}
.btn{display:inline-block;background:var(--red);color:var(--white);font-weight:700;font-size:13px;padding:9px 20px;border-radius:2px}
.ph{display:block}

/* header */
.topbar{height:28px;background:var(--white);border-bottom:1px solid var(--line);font-size:11px;color:var(--muted)}
.topbar .wrap{display:flex;gap:30px;align-items:center;height:28px;padding-left:200px}
.masthead{height:114px;background:var(--white)}
.masthead .wrap{display:flex;align-items:center;height:114px;justify-content:space-between}
.brand{display:flex;align-items:center;gap:12px}
.brand-dot{width:40px;height:40px;border-radius:50%;background:var(--teal)}
.brand-name{font-family:"Raleway",sans-serif;font-weight:700;font-size:28px;color:var(--teal)}
.brand-tag{font-size:11px;color:var(--muted);margin-top:-4px}
.mainnav{display:flex;gap:30px;align-items:center;font-size:13px;font-weight:600;color:var(--ink)}
.mainnav .active{color:var(--red);border-bottom:2px solid var(--red)}
.phone{display:flex;align-items:center;gap:6px;font-weight:700;color:var(--teal)}
.cart{background:var(--red);color:var(--white);padding:6px 14px;font-size:12px}
.subnav{height:43px;background:var(--teal)}
.subnav .wrap{display:flex;height:43px;align-items:stretch}
.subnav a{flex:auto;display:flex;align-items:center;justify-content:center;color:var(--white);font-size:12px;font-weight:700;text-transform:uppercase;border-right:1px solid rgba(255,255,255,.25)}
.subnav a:last-child{border-right:0}

/* hero */
.hero{height:527px;position:relative}
.hero .ph{position:absolute;inset:0;width:1030px;left:50%;margin-left:-515px;background:linear-gradient(120deg,#e4f3f7 0%,#bfe3ef 40%,#d9c9b8 70%,#a98c74 100%)}
.hero-copy{position:absolute;left:20px;top:130px}
.hero-copy h1{font-size:62px;line-height:1.05;font-weight:400;color:var(--teal);margin-bottom:34px}
.hero-seal{position:absolute;left:20px;top:410px;width:46px;height:46px;border-radius:50%;background:var(--teal-soft)}

/* feature cards */
.features{height:445px;padding-top:43px}
.features .wrap{display:flex;justify-content:space-between}
.fcard{width:313px;height:331px;background:var(--white);position:relative}
.fcard .ph{height:200px}
.fcard-body{position:absolute;top:165px;left:18px;right:18px;background:var(--white);padding:12px 14px;font-size:12px;line-height:1.45}
.fcard-body small{color:var(--muted)}
.fcard-body h3{font-size:17px;color:var(--teal);font-weight:600;margin-bottom:4px}
.fcard-body .btn{padding:5px 12px;font-size:11px;margin-top:8px}

/* main */
.main{height:2880px}
.main .wrap{display:flex;justify-content:space-between;padding-top:12px}
.content{width:622px}
.content h2{font-size:32px;line-height:1.25;color:var(--teal);font-weight:700;margin-bottom:22px}
.content p{margin-bottom:16px;font-size:14.5px}
.content h4{font-size:15px;margin:26px 0 14px;color:var(--ink)}
.issues{display:grid;grid-template-columns:1fr 1fr;column-gap:30px;list-style:none;font-size:14px;margin-bottom:26px}
.issues li{padding-left:16px;position:relative;line-height:1.85}
.issues li:before{content:"";position:absolute;left:0;top:10px;width:6px;height:6px;border-radius:50%;background:var(--teal)}
.issues li:empty:before{display:none}
.block{margin-bottom:80px}
.locations{display:grid;grid-template-columns:1fr 1fr;list-style:none;font-size:14px;margin:0 0 18px 30px;width:470px}
.locations li{line-height:1.9}
.locations li:not(:empty):before{content:"• ";color:var(--teal)}
.wide-photo{height:146px;margin:28px 0 34px;background:linear-gradient(90deg,#dfe7ea,#c9a893 30%,#f2e8df 55%,#b59079 80%,#dfe7ea)}
.section-head{font-size:21px;color:var(--teal);font-weight:700;margin-bottom:16px}
.aside-photo{display:flex;align-items:center;height:160px;margin:36px 0 40px;background:var(--white)}
.aside-photo .ph{width:330px;height:160px;background:linear-gradient(90deg,#f4efe9,#b9957d)}
.aside-photo span{padding-left:40px;color:var(--teal);font-style:italic;font-size:15px}
.links{list-style:none;margin:0 0 18px 20px;font-size:14px}
.links li{color:var(--teal);line-height:1.8}
.links li:before{content:"› ";color:var(--red)}
.quote{font-size:23px;font-style:italic;color:var(--teal);font-family:"Raleway",sans-serif;margin:30px 0 30px}
.author{display:flex;gap:24px;align-items:flex-start}
.author .ph{width:130px;height:110px;flex:none;background:linear-gradient(160deg,#e3dad1,#9c7c66)}
.author p{margin-bottom:6px;font-size:13.5px}
.author .sign{font-size:12px;color:var(--muted);line-height:1.5}

/* sidebar */
.sidebar{width:335px}
.finder{background:var(--red);color:var(--white);padding:22px 22px 26px;margin-bottom:52px}
.finder h3{font-size:19px;text-align:center;margin-bottom:20px;font-weight:700;line-height:1.2}
.field{height:40px;background:var(--white);color:var(--muted);font-size:12px;padding:0 14px;display:flex;align-items:center;justify-content:space-between;margin-bottom:14px}
.finder .btn{display:block;width:150px;margin:20px auto 0;background:var(--red-dark);text-align:center;font-size:16px}
.video{height:285px;background:linear-gradient(160deg,#7fb6c2,#3d6d7a);position:relative;margin-bottom:14px}
.video span{position:absolute;left:14px;top:10px;color:var(--white);font-size:13px}
.video svg{position:absolute;left:50%;top:50%;margin:-28px 0 0 -28px}
.rebates h4{color:var(--teal);font-size:15px;margin-bottom:10px}
.badges{display:grid;grid-template-columns:1fr 1fr;gap:14px 20px;margin-bottom:14px}
.badges i{display:block;height:48px;border-radius:4px}
.rebates .btn{display:table;margin:0 auto 30px}
.blog h3{font-size:28px;color:var(--teal);margin-bottom:22px}
.post{display:flex;gap:18px;padding:12px 0;border-bottom:1px solid var(--line);min-height:112px}
.post .ph{width:76px;height:76px;flex:none;background:linear-gradient(140deg,#eadfd6,#a88672)}
.post h5{font-size:15px;line-height:1.3;color:var(--teal);font-weight:700;font-family:"Raleway",sans-serif}
.post small{display:block;font-size:11px;color:var(--muted);margin:4px 0}
.post .btn{padding:3px 10px;font-size:10px}
.blog .all{display:table;margin:26px auto 0}

/* article cards */
.articles{height:860px;border-top:1px solid var(--line);padding-top:30px}
.articles .wrap{display:grid;grid-template-columns:repeat(3,300px);justify-content:space-between;row-gap:40px}
.acard{background:var(--white);height:400px;text-align:center;padding-top:40px;border:1px solid var(--line)}
.acard .ph{width:180px;height:180px;border-radius:50%;margin:0 auto 34px;background:linear-gradient(140deg,#e6ddd5,#9f7f6a)}
.acard h3{font-size:17px;color:var(--teal);line-height:1.3;height:66px;padding:0 40px}
.acard .btn{padding:6px 20px;font-size:12px}

/* footer */
.footer{height:318px;background:var(--teal);color:var(--white);padding-top:40px}
.footer .wrap{display:flex;gap:80px}
.footer h4{font-size:18px;margin-bottom:14px}
.footer ul{list-style:none;font-size:14px;line-height:1.75}
.footer li{display:flex;align-items:center;gap:10px}
.dot{width:16px;height:16px;border-radius:50%;background:var(--white);opacity:.85;flex:none}
.login{width:300px;margin-left:auto}
.login .field{margin-bottom:10px}
.login .btn{padding:7px 24px}
.legal{height:100px;background:var(--teal-dark);color:var(--white);font-size:12px;text-align:center;padding-top:24px}
.legal nav{display:flex;gap:36px;justify-content:center;margin-top:8px}
</style>
</head>
<body>

<header>
  <div class="topbar"><div class="wrap"><span>JOIN OUR ASSOCIATE PROGRAM</span><span>MARRIAGE COUNSELLING</span><span>RELATIONSHIP COUNSELLING</span></div></div>
  <div class="masthead"><div class="wrap">
    <div>
      <div class="brand"><span class="brand-dot"></span><span class="brand-name">The Willow Nook</span></div>
      <div class="brand-tag" style="padding-left:52px">helping you create loving relationships</div>
    </div>
    <nav class="mainnav">
      <a class="active">HOME</a><a>ABOUT</a><a>RESOURCES</a><a>BLOG</a>
      <span class="cart">CART</span>
      <span class="phone"><svg width="14" height="14" viewBox="0 0 24 24"><path fill="#1b8b92" d="M6.6 10.8a15 15 0 006.6 6.6l2.2-2.2a1 1 0 011-.25 11 11 0 003.6.6 1 1 0 011 1V20a1 1 0 01-1 1A17 17 0 013 4a1 1 0 011-1h3.5a1 1 0 011 1c0 1.25.2 2.45.6 3.6a1 1 0 01-.25 1z"/></svg>1300 555 014</span>
    </nav>
  </div></div>
  <nav class="subnav"><div class="wrap">
    <a>Counselling Types</a><a>Relationship Counselling Location</a><a>See Therapy Location</a><a>Quizzes</a><a>FAQ</a><a>Contact</a>
  </div></nav>
</header>

<section class="hero">
  <div class="ph" role="img" aria-label="Photo of a smiling couple outdoors, the man carrying the woman on his back"></div>
  <div class="wrap">
    <div class="hero-copy">
      <h1>Helping You<br>Create Loving<br>Relationship</h1>
      <a class="btn">CONTACT US</a>
    </div>
    <span class="hero-seal"></span>
  </div>
</section>

<section class="features"><div class="wrap">
  <article class="fcard"><div class="ph" role="img" aria-label="Photo of a couple embracing" style="background:linear-gradient(140deg,#efe6dd,#b48f76)"></div>
    <div class="fcard-body"><small>Do you need help</small><h3>Relationship Counselling</h3>Communication, reconnecting, trust and intimacy. Build calm, honest talk.<br><a class="btn">Read More</a></div></article>
  <article class="fcard"><div class="ph" role="img" aria-label="Photo of a couple relaxing together" style="background:linear-gradient(140deg,#e9eef0,#a9876f)"></div>
    <div class="fcard-body"><small>Do you need help</small><h3>Sex Therapy Counselling</h3>Low desire, mismatched needs, closeness and renewed connection together.<br><a class="btn">Read More</a></div></article>
  <article class="fcard"><div class="ph" role="img" aria-label="Photo of a thoughtful woman" style="background:linear-gradient(140deg,#f1ece6,#c19c84)"></div>
    <div class="fcard-body"><small>Do you need help</small><h3>Narcissism Counselling</h3>Managing narcissistic traits, anger and lack of empathy in a partner.<br><a class="btn">Read More</a></div></article>
</div></section>

<section class="main"><div class="wrap">
  <div class="content">
    <div class="block">
      <h2>We Specialise In Relationship &amp;<br>Marriage Counselling</h2>
      <p>At The Willow Nook, we are a group of psychologists, Australia wide, who are passionate about relationships and helping you with yours.</p>
      <p>Our vision is to provide the most highly regarded and comprehensive marriage counselling and relationship counselling, and sex therapy in Australia, at reasonable and affordable rates.</p>
      <p>When we are experiencing relationship and marriage problems, there can be a lot of pain and confusion, and it can often be difficult to cope with the other areas of our lives when we are struggling.</p>
      <a class="btn">Read More</a>
    </div>
    <div class="block">
      <h2>Our Willow Nook Relationship Psychologist</h2>
      <p>Our team of hand chosen Registered Psychologists in locations across Australia are individually selected for their knowledge, experience, compassion, and unbiased approach to marriage counselling and sexual therapy.</p>
      <h4>Here are some of the common ones:</h4>
      <ul class="issues">
        <li>Affairs</li><li>Problems with parenting your children</li>
        <li>Controlling behaviour</li><li>Step children and in-laws</li>
        <li>Verbal abuse</li><li>All forms of family problems</li>
        <li>Imbalance of power</li><li>Anger management problems</li>
        <li>Lack of intimacy</li><li>Porn addiction problems</li>
        <li>Poor communication</li><li>Pre-marriage preparations</li>
        <li>Loss of love</li><li>Narcissism problems</li>
        <li>Relationship neglect</li><li></li>
        <li>Sexual problems</li><li></li>
        <li>Problems from childhood</li><li></li>
      </ul>
      <a class="btn">Read More</a>
    </div>
    <div>
      <h2>Our Relationship Counselling Locations across Australia</h2>
      <p>We currently have relationship counselling and marriage counselling services in:</p>
      <ul class="locations">
        <li>Sydney – 19 centres</li><li>Adelaide – 4 centres</li>
        <li>Canberra – 2 centres</li><li>Gold Coast – 5 centres</li>
        <li>Melbourne – 21 centres</li><li>Sunshine Coast – 2 centres</li>
        <li>Perth – 11 centres</li><li>Cairns – 1 centre</li>
        <li>Brisbane – 14 centres</li><li>Townsville – 1 centre</li>
        <li>Wollongong – 1 centre</li><li>Mudgee – 1 centre</li>
        <li>Central Coast – 2 centres</li><li></li>
      </ul>
      <p>Certain clinics also provide after hours and Saturday sessions for your convenience. Click the Locations tab for more information about one.</p>
      <div class="wide-photo ph" role="img" aria-label="Photo banner of smiling couples"></div>
      <h3 class="section-head">Communication is a vital skill but often not taught to us.</h3>
      <p>Most people find that their ways of communicating with each other are what hamper us from having a happy healthy relationship.</p>
      <p>Effective interpersonal communication skills are not something that we are usually taught. But for almost everyone who is having difficulties in their relationship, they feel that they are trying to communicate their thoughts and feelings but their partner is not listening.</p>
      <p>Most people then find that they themselves don't want to listen when they experience their partner as not wanting to listen to them, so the net effect is that neither person gets listened to, and both are frustrated.</p>
      <p>So learning how to communicate your honest thoughts and feelings in a way that your partner does truly listen is a crucial skill for you to feel that you are in a fulfilling relationship. We can show you some simple but effective principles on how to do this with each other.</p>
      <div class="aside-photo"><div class="ph" role="img" aria-label="Photo of a reflective woman"></div><span>Individual help and guidance<br>on your relationship</span></div>
      <h3 class="section-head">We as individuals have specific patterns in our relationships.</h3>
      <p>We can also assist you if you want individual help and guidance on your relationship, so you can learn what the patterns in your relationships are showing you about yourself.</p>
      <p>Want more information? Please help yourself to our free articles on common relationship problems you may be encountering including:</p>
      <ul class="links">
        <li>Why relationships go wrong</li><li>How to recover from an affair</li><li>Have you lost yourself in your relationship</li><li>The secret to more sex</li>
      </ul>
      <p>For the latest short, up-to-date articles on relationships, relationship problems and relationship counselling, please also check out our relationship counselling blog.</p>
      <p class="quote">“ At the end of our life, what matters most is how well did we love”</p>
      <div class="author">
        <div class="ph" role="img" aria-label="Portrait photo of the director"></div>
        <div><p>You can read more about relationship counselling here.</p><p>Warmly</p><p class="sign">Maren Ellis<br>Director – Psychologist<br>Grad Dip Psych, Post Grad Dip Psych, B.Ed, Dip Teach, MAPS</p></div>
      </div>
    </div>
  </div>

  <aside class="sidebar">
    <div class="finder">
      <h3>FIND OUR PSYCHOLOGIST<br>NEAR YOU</h3>
      <div class="field">Types of Counselling <span>▾</span></div>
      <div class="field">Location</div>
      <div class="field">Postcode</div>
      <a class="btn">SEARCH</a>
    </div>
    <div class="video ph" role="img" aria-label="Video preview: what to expect from counselling"><span>What To Expect From Counselling</span>
      <svg width="56" height="56" viewBox="0 0 56 56"><circle cx="28" cy="28" r="27" fill="none" stroke="#fff" stroke-width="2"/><path d="M23 18l14 10-14 10z" fill="#fff"/></svg></div>
    <div class="rebates">
      <h4>Rebates Available</h4>
      <div class="badges"><i style="background:#1b8b92"></i><i style="background:#e0242c"></i><i style="background:#87cfc6"></i><i style="background:#2b5f9e"></i><i style="background:#3d4a50"></i><i style="background:#5aa84a"></i></div>
      <a class="btn">More</a>
    </div>
    <div class="blog">
      <h3>Our Blog</h3>
      <div class="post"><div class="ph" role="img" aria-label="Blog thumbnail photo"></div><div><h5>What can I do if I'm living with a Narcissist?</h5><small>Feb 24, 2017</small><a class="btn">Read More</a></div></div>
      <div class="post"><div class="ph" role="img" aria-label="Blog thumbnail photo"></div><div><h5>Why am I with a Narcissist?</h5><small>Feb 24, 2017</small><a class="btn">Read More</a></div></div>
      <div class="post"><div class="ph" role="img" aria-label="Blog thumbnail photo"></div><div><h5>How Do I Know If I'm With a Narcissist?</h5><small>Feb 24, 2017</small><a class="btn">Read More</a></div></div>
      <div class="post"><div class="ph" role="img" aria-label="Blog thumbnail photo"></div><div><h5>Are You living with a Stonewaller</h5><small>Feb 24, 2017</small><a class="btn">Read More</a></div></div>
      <div class="post"><div class="ph" role="img" aria-label="Blog thumbnail photo"></div><div><h5>Letter for a Partner Doubtful About Relationship Counselling</h5><small>Feb 24, 2017</small><a class="btn">Read More</a></div></div>
      <div class="post"><div class="ph" role="img" aria-label="Blog thumbnail photo"></div><div><h5>Do You Wonder Why You and Your Partner Are Together?</h5><small>Feb 24, 2017</small><a class="btn">Read More</a></div></div>
      <div class="post"><div class="ph" role="img" aria-label="Blog thumbnail photo"></div><div><h5>Did Your Relationship Start on Rocky Ground</h5><small>Feb 24, 2017</small><a class="btn">Read More</a></div></div>
      <div class="post"><div class="ph" role="img" aria-label="Blog thumbnail photo"></div><div><h5>What Are You Like In a Relationship?</h5><small>Feb 24, 2017</small><a class="btn">Read More</a></div></div>
      <div class="post"><div class="ph" role="img" aria-label="Blog thumbnail photo"></div><div><h5>Is Your Pursuit of Success Sabotaging Your Relationships That Matter Most?</h5><small>Feb 24, 2017</small><a class="btn">Read More</a></div></div>
      <div class="post"><div class="ph" role="img" aria-label="Blog thumbnail photo"></div><div><h5>Letter for a Partner Doubtful About Relationship Counselling</h5><small>Feb 24, 2017</small><a class="btn">Read More</a></div></div>
      <div class="post"><div class="ph" role="img" aria-label="Blog thumbnail photo"></div><div><h5>Do You Wonder Why You and Your Partner Are Together?</h5><small>Feb 24, 2017</small><a class="btn">Read More</a></div></div>
      <div class="post"><div class="ph" role="img" aria-label="Blog thumbnail photo"></div><div><h5>Did Your Relationship Start on Rocky Ground</h5><small>Feb 24, 2017</small><a class="btn">Read More</a></div></div>
      <a class="btn all">View All Blogs</a>
    </div>
  </aside>
</div></section>

<section class="articles"><div class="wrap">
  <article class="acard"><div class="ph" role="img" aria-label="Round photo of a distressed couple"></div><h3>How to deal with an affair?</h3><a class="btn">Learn More</a></article>
  <article class="acard"><div class="ph" role="img" aria-label="Round photo of a same sex couple"></div><h3>Same Sex Relationships &amp; Counselling</h3><a class="btn">Learn More</a></article>
  <article class="acard"><div class="ph" role="img" aria-label="Round photo of an upset woman"></div><h3>Are you living with a narcissist?</h3><a class="btn">Learn More</a></article>
  <article class="acard"><div class="ph" role="img" aria-label="Round photo of a couple turned away from each other"></div><h3>Is one of you an Intimacy Withholder</h3><a class="btn">Learn More</a></article>
  <article class="acard"><div class="ph" role="img" aria-label="Round photo of a man at a laptop"></div><h3>Is too much porn affecting your relationship</h3><a class="btn">Learn More</a></article>
  <article class="acard"><div class="ph" role="img" aria-label="Round photo of a worried woman"></div><h3>Safe Relationships. Is your relationship safe?</h3><a class="btn">Learn More</a></article>
</div></section>

<footer>
  <div class="footer"><div class="wrap">
    <div><h4>Quick Links</h4><ul><li>Home</li><li>About</li><li>Blog</li><li>Resources</li><li>Contact</li></ul></div>
    <div><h4>Contact Us</h4><ul>
      <li><svg width="16" height="16" viewBox="0 0 24 24"><path fill="#fff" d="M6.6 10.8a15 15 0 006.6 6.6l2.2-2.2a1 1 0 011-.25 11 11 0 003.6.6 1 1 0 011 1V20a1 1 0 01-1 1A17 17 0 013 4a1 1 0 011-1h3.5a1 1 0 011 1c0 1.25.2 2.45.6 3.6a1 1 0 01-.25 1z"/></svg>1300 555 014</li>
      <li><svg width="16" height="16" viewBox="0 0 24 24"><rect x="2" y="5" width="20" height="14" rx="1" fill="none" stroke="#fff" stroke-width="2"/><path d="M2 6l10 7 10-7" fill="none" stroke="#fff" stroke-width="2"/></svg>hello@thewillownook.com.au</li>
    </ul></div>
    <div><h4>Follow Us</h4><ul><li><span class="dot"></span>Community</li><li><span class="dot"></span>Updates</li><li><span class="dot"></span>Network</li></ul></div>
    <div class="login"><h4>Login</h4><div class="field">Username</div><div class="field">Password</div><a class="btn">Login</a></div>
  </div></div>
  <div class="legal">© Copyright The Willow Nook 2017
    <nav><a>Privacy Policy</a><a>Terms &amp; Conditions</a><a>Site Map</a><a>Associate Psychologists Program</a><a>Contact Us</a></nav>
  </div>
</footer>

</body>
</html>
```